Vodka Soda brand identity design and label design

New vodka soda (hard seltzer) brand needs a brand identity design and label designs.

The brand name is VELMO

We produce vodka soda packaged in cans. They come in three flavours
- Raspberry and Lime
- Pina Colada
- Black Cherry

We would like to have the designs look similar (same template) but have one difference depending on the fruit flavour.

The final delivered package should contain
- brand identity design guide with a logo, font and colour schemes
- 3 label designs on the same template (label size 8.125 x 5 inches)

Some example designs of similar products are attached to the project.

Target Market(s)

Gender neutral, younger population

Colors
000000

Requirements
Must have
• Bright background and bright eye catching colours.

```html
<!DOCTYPE html>
<html lang="en">
<head>
<meta charset="UTF-8">
<title>VELMO Hard Seltzer – Raspberry &amp; Lime Label</title>
<link rel="stylesheet" href="https://fonts.googleapis.com/css2?family=Poppins:wght@300;400;700&display=swap">
<style>
  :root {
    --backdrop: #d9c9ca;
    --label-white: #ffffff;
    --ink-black: #1e1c1d;
    --flavour-red: #e31b37;
    --pattern-grey: #e6e6e6;
  }
  html, body {
    margin: 0;
    padding: 0;
    width: 1200px;
    height: 1200px;
    overflow: hidden;
    background: var(--backdrop);
  }
  .canvas {
    position: relative;
    width: 1200px;
    height: 1200px;
  }
  .label {
    position: absolute;
    left: 292px;
    top: 100px;
    width: 616px;
    height: 1000px;
    box-shadow: 0 2px 6px rgba(0,0,0,0.15);
    background: var(--label-white);
  }
  .label svg {
    display: block;
    width: 100%;
    height: 100%;
  }
  .brand-name {
    font-family: "Poppins", sans-serif;
    font-weight: 700;
    fill: var(--ink-black);
  }
  .product-type {
    font-family: "Poppins", sans-serif;
    font-weight: 700;
    fill: var(--flavour-red);
  }
  .flavour-name {
    font-family: "Poppins", sans-serif;
    font-weight: 700;
    fill: var(--ink-black);
  }
  .flavour-note {
    font-family: "Poppins", sans-serif;
    font-weight: 400;
    fill: var(--ink-black);
  }
  .info-band {
    fill: var(--flavour-red);
  }
  .info-text {
    font-family: "Poppins", sans-serif;
    font-weight: 300;
    fill: var(--label-white);
  }
</style>
</head>
<body>
<div class="canvas">
  <div class="label">
    <svg viewBox="0 0 812 1318" xmlns="http://www.w3.org/2000/svg">
      <defs>
        <linearGradient id="patternFade" x1="0" y1="0" x2="0" y2="1">
          <stop offset="0" stop-color="#e9e9e9"/>
          <stop offset="0.55" stop-color="#f5f5f5"/>
          <stop offset="1" stop-color="#ffffff"/>
        </linearGradient>
      </defs>

      <rect class="label-base" x="0" y="0" width="812" height="1318" fill="var(--label-white)"/>

      <rect class="decor-pattern" x="0" y="0" width="812" height="720" fill="url(#patternFade)"
            role="img" aria-label="Soft grey curved lattice pattern fading into white"/>

      <text class="brand-name" transform="translate(411 1012) rotate(-90)"
            font-size="215" textLength="899" lengthAdjust="spacingAndGlyphs">VELMO</text>

      <text class="product-type" transform="translate(489 892) rotate(-90)"
            font-size="82" textLength="662" lengthAdjust="spacing">HARD SELTZER</text>

      <text class="flavour-name" x="406" y="1128" font-size="40" text-anchor="middle">RASPBERRY &amp; LIME</text>
      <text class="flavour-note" x="410" y="1189" font-size="30" text-anchor="middle">WITH ANTIOXIDANT</text>
      <text class="flavour-note" x="410" y="1226" font-size="30" text-anchor="middle">VITAMIN C</text>

      <rect class="info-band" x="0" y="1245" width="812" height="73"/>
      <text class="info-text" x="130" y="1292" font-size="27" text-anchor="middle">5% alc/vol</text>
      <text class="info-text" x="406" y="1292" font-size="27" text-anchor="middle">12 fl. oz.(355 ml)</text>
      <text class="info-text" x="660" y="1292" font-size="27" text-anchor="middle">HARD SELTZER</text>
    </svg>
  </div>
</div>
</body>
</html>
```